Brightwave Audiology Letterhead redesign project

We need a full redesign of our current letterhead to make it consistent with the look and feel of our website design www.brightwaveaudio.com.au. It will need to include all information on the current version attached. The letterhead is used for sending medical reports and general correspondence. It should make use of our corporate colours (purple and teal) as per the logo on the existing file. The letterhead should be bold and eye-catching.

Target Market(s)

Medical practitioners.

Font styles to use
Sans Serif

Requirements
Must have
• It will need to include all information on the current version. Must have a premium, professional, high-end look and feel.
Nice to have
• Bold and eye-catching letterhead that reinforces the Brightwave Audiology brand. To stand out from other traditional letterheads.
Should not have
• The design should not be too cluttered or 'busy'

```html
<!DOCTYPE html>
<html lang="en">
<head>
<meta charset="utf-8">
<title>Brightwave Audiology Letterhead</title>
<link href="https://fonts.googleapis.com/css2?family=Open+Sans:wght@400;600;700;800&display=swap" rel="stylesheet">
<style>
  :root {
    --purple: #6a2a9a;
    --purple-light: #8b4cba;
    --teal: #0f9a78;
    --ink: #5a5a5a;
    --paper: #ffffff;
    --backdrop: #ecebf2;
    --mark: #efefef;
    --badge: #e2e2e8;
  }
  * { margin: 0; padding: 0; box-sizing: border-box; }
  html, body { width: 1200px; height: 784px; overflow: hidden; }
  body {
    background: var(--backdrop);
    font-family: "Open Sans", Arial, sans-serif;
    position: relative;
  }
  .letterhead {
    position: absolute;
    left: 340px;
    top: 24px;
    width: 520px;
    height: 736px;
    background: var(--paper);
    box-shadow: 0 2px 10px rgba(60, 40, 100, 0.12);
    overflow: hidden;
  }
  .header-rule-teal {
    position: absolute; left: 0; top: 34px;
    width: 34px; height: 5px; background: var(--teal);
  }
  .brand-name {
    position: absolute; left: 42px; top: 20px;
    font-weight: 800; font-size: 24px; letter-spacing: -0.3px;
    color: var(--purple);
  }
  .header-rule-purple {
    position: absolute; left: 320px; top: 34px;
    width: 38px; height: 7px; background: var(--purple);
  }
  .practitioners {
    position: absolute; right: 22px; top: 56px;
    text-align: right; font-size: 8.5px; line-height: 1.45;
    color: var(--ink); text-transform: uppercase; letter-spacing: 0.2px;
  }
  .practitioners-title { color: var(--teal); font-weight: 700; }
  .header-edge-bar {
    position: absolute; right: 0; top: 100px;
    width: 44px; height: 7px; background: var(--purple);
  }
  .faint-mark {
    position: absolute; left: 190px; top: 296px;
    width: 140px; height: 140px; border-radius: 50%;
    background: var(--mark);
  }
  .footer-graphics { position: absolute; left: 0; bottom: 0; }
  .contact-line {
    position: absolute; left: 14px; bottom: 72px;
    font-size: 8.5px; color: var(--ink);
    display: flex; gap: 8px; align-items: center;
  }
  .contact-item { display: flex; align-items: center; gap: 3px; }
  .contact-dot {
    width: 7px; height: 7px; border-radius: 50%; background: var(--purple-light);
  }
  .accreditation-badge {
    position: absolute; right: 22px; bottom: 56px;
    width: 44px; height: 20px; border-radius: 3px;
    background: var(--badge);
  }
  .website {
    position: absolute; right: 22px; bottom: 11px;
    font-weight: 700; font-size: 11px; color: #fff;
  }
</style>
</head>
<body>
  <main class="letterhead">
    <div class="header-rule-teal"></div>
    <div class="brand-name">Brightwave Audiology</div>
    <div class="header-rule-purple"></div>

    <div class="practitioners">
      <div class="practitioners-title">Clinical Audiologists</div>
      <div>Daniel Marsh BMus, MAudSt, MAudSA (CCP)</div>
      <div>Oliver Marsh BN, Grad Dip FET, MAudSt, MAudSA (CCP)</div>
    </div>
    <div class="header-edge-bar"></div>

    <div class="faint-mark" role="img" aria-label="Faint circular brand decoration"></div>

    <div class="contact-line">
      <span class="contact-item"><span class="contact-dot"></span>48 Carrow Lane Ashford, Qld 4361</span>
      <span class="contact-item"><span class="contact-dot"></span>07 4510 2284</span>
      <span class="contact-item"><span class="contact-dot"></span>07 95127740</span>
      <span class="contact-item"><span class="contact-dot"></span>hello@brightwaveaudio.com.au</span>
    </div>

    <div class="accreditation-badge" role="img" aria-label="Professional accreditation badge"></div>

    <svg class="footer-graphics" width="520" height="64" viewBox="0 0 520 64" aria-hidden="true">
      <polyline points="0,8 118,8 126,16 216,16 224,24 330,24 338,32 520,32" fill="none" stroke="var(--teal)" stroke-width="3"/>
      <polygon points="0,22 112,22 120,30 210,30 218,38 330,38 336,34 520,34 520,64 0,64" fill="var(--purple)"/>
    </svg>
    <div class="website">www.brightwaveaudio.com.au</div>
  </main>
</body>
</html>
```